Travel Company is looking for a STAND OUT Business Card

I need a unique Business Card that will truly stand out. Nothing too busy. Simple is good, right? Not looking for a standard design either. No cookie cutter layout. We are a Travel Company that works more with Companies than Travelers. I had an idea to focus and emphasis on the 2 logo a bit more. This is not necessary, however thought it would look interesting. I am just looking for something interesting and a bit different. Does't have to completely off the wall crazy, just not your run of the mill business card.

Target Market(s)

Hoteliers, Resort Management, Call Centers, Executives, Travelers, Families, Businesses

Industry/Entity Type

Hospitality

Contact Information for Business Card

President/CEO - Marcus T Bellamy (title not necessary if design doesn't allow for it)
contact - (407) 555-0186
email - mbellamy@wayfarenow.example
address - 4812 Quillmore Ave #164
Orlando, FL 32804
website - www.wayfarenow.example

Font styles to use
Serif
Other font styles liked:
• Avenir Next LT Pro BOLD

Requirements
Must have
• simple look and design. Unique design
Nice to have
• I attached the 2 logo separate from the main logo. This can be used separately from the Main Logo, together with the main logo or as main logo. I included the logo font. Use it or not, designers choice.
Should not have
• cookie cutter design. Little use of red other than the logo

```html
<!DOCTYPE html>
<html lang="en">
<head>
<meta charset="utf-8">
<title>Wayfare Now — Business Card</title>
<link rel="stylesheet" href="https://fonts.googleapis.com/css2?family=Source+Sans+3:wght@400;700&display=swap">
<style>
  :root {
    --bg: #4a4a4a;
    --card-front: #ffffff;
    --card-back: #070809;
    --ink: #0b0b0b;
    --accent: #ec1c24;
    --text-light: #ffffff;
  }
  * { margin: 0; padding: 0; box-sizing: border-box; }
  html, body { width: 1200px; height: 1200px; overflow: hidden; }
  body {
    background: var(--bg);
    font-family: "Source Sans 3", sans-serif;
    position: relative;
  }
  .card {
    position: absolute;
    left: 250px;
    width: 700px;
    height: 397px;
    border-radius: 20px;
    overflow: hidden;
  }
  .card--front { top: 165px; background: var(--card-front); }
  .card--back { top: 638px; background: var(--card-back); color: var(--text-light); }

  .brand {
    position: absolute;
    inset: 0;
    display: flex;
    align-items: center;
    justify-content: center;
    gap: 18px;
  }
  .brand__dot {
    width: 46px; height: 46px;
    border-radius: 50%;
    background: var(--accent);
  }
  .brand__name {
    font-weight: 700;
    font-size: 68px;
    letter-spacing: -1.5px;
    color: var(--ink);
    line-height: 1;
  }

  .back__disc {
    position: absolute;
    left: -60px;
    top: 60px;
    width: 330px;
    height: 330px;
    border-radius: 50%;
    background: var(--accent);
  }

  .contact {
    position: absolute;
    left: 342px;
    top: 124px;
  }
  .contact__name {
    font-weight: 700;
    font-size: 30px;
    color: var(--accent);
    line-height: 1;
  }
  .contact__title {
    font-size: 18px;
    margin-top: 4px;
  }
  .contact__list {
    list-style: none;
    margin-top: 34px;
  }
  .contact__list li {
    display: flex;
    align-items: center;
    gap: 12px;
    font-size: 18px;
    height: 25px;
  }
  .contact__list svg { width: 18px; height: 18px; flex: none; }
  .contact__address {
    font-style: normal;
    font-size: 18px;
    line-height: 24px;
    margin-top: 22px;
    margin-left: -3px;
  }
</style>
</head>
<body>
  <section class="card card--front">
    <div class="brand">
      <span class="brand__dot"></span>
      <span class="brand__name">wayfare now</span>
    </div>
  </section>

  <section class="card card--back">
    <div class="back__disc"></div>
    <div class="contact">
      <h1 class="contact__name">Marcus T Bellamy</h1>
      <p class="contact__title">President/CEO</p>
      <ul class="contact__list">
        <li>
          <svg viewBox="0 0 20 20" aria-hidden="true"><path fill="#ec1c24" d="M2 7c0-3 4-4 8-4s8 1 8 4v2h-4V7.5H6V9H2z"/><path fill="#ec1c24" d="M5 10h10l2 7H3z"/><circle cx="10" cy="13.5" r="2" fill="#070809"/></svg>
          (407) 555-0186
        </li>
        <li>
          <svg viewBox="0 0 20 20" aria-hidden="true"><rect x="1" y="4" width="18" height="12" fill="#ec1c24"/><path d="M1 4l9 7 9-7M1 16l7-6M19 16l-7-6" stroke="#070809" stroke-width="1.4" fill="none"/></svg>
          mbellamy@wayfarenow.example
        </li>
        <li>
          <svg viewBox="0 0 20 20" aria-hidden="true"><g fill="none" stroke="#ec1c24" stroke-width="1.4"><circle cx="10" cy="10" r="8.3"/><ellipse cx="10" cy="10" rx="3.6" ry="8.3"/><path d="M2 10h16M3.3 6h13.4M3.3 14h13.4"/></g></svg>
          www.wayfarenow.example
        </li>
      </ul>
      <address class="contact__address">
        4812 Quillmore Ave #164<br>
        Orlando, FL 32804
      </address>
    </div>
  </section>
</body>
</html>
```